Business Card Design

We have recently seen two business cards that caught our attention and think the designs would work for us. We are an accounting firm that serves small businesses in a variety of industries. Attached are the two business card that inspired us along with very rough layouts. We would like to see a professional layout using our company information.

Industry/Entity Type

Accounting

Contact Information for Business Card

Company Name - Dalworth Pryce
Address - 4180 Brambleton Lane, Suite 310, Houston, TX 77051
713-508-9627 - Main
281-369-0714 - Fax

Team Member Names, emails and phone numbers (see attachment)

```html
<!DOCTYPE html>
<html lang="en">
<head>
<meta charset="utf-8">
<title>Dalworth Pryce — Business Card</title>
<link rel="stylesheet" href="https://fonts.googleapis.com/css2?family=Jost:wght@300;400&display=swap">
<style>
  :root {
    --stage-centre: #ffffff;
    --stage-edge: #e6e7e8;
    --card-bg: #ffffff;
    --card-border: #8a8b8d;
    --ink: #231f20;
    --ink-soft: #6d6e71;
    --rule: #9d9fa2;
  }
  * { margin: 0; padding: 0; box-sizing: border-box; }
  html, body {
    width: 1200px;
    height: 703px;
    overflow: hidden;
  }
  body {
    background: radial-gradient(ellipse at center, var(--stage-centre) 45%, var(--stage-edge) 100%);
    font-family: "Jost", "Futura", sans-serif;
    font-weight: 300;
    color: var(--ink-soft);
    position: relative;
  }
  .card {
    position: absolute;
    left: 168px;
    top: 112px;
    width: 864px;
    height: 485px;
    background: var(--card-bg);
    border: 1px solid var(--card-border);
  }
  .brand {
    position: absolute;
    left: 55px;
    top: 149px;
    font-weight: 400;
    font-size: 22px;
    letter-spacing: 2.4px;
    color: var(--ink);
    line-height: 1;
    white-space: nowrap;
  }
  .person {
    position: absolute;
    left: 55px;
    top: 296px;
  }
  .person__name {
    font-size: 26px;
    font-weight: 300;
    color: var(--ink);
    line-height: 30px;
  }
  .person__role {
    font-size: 19px;
    line-height: 26px;
    margin-bottom: 6px;
  }
  .contact-line {
    font-size: 22px;
    line-height: 30px;
    white-space: nowrap;
  }
  .contact-line__label {
    display: inline-block;
    width: 26px;
    font-size: 15px;
    font-weight: 400;
    color: var(--ink);
    padding-left: 2px;
  }
  .office {
    position: absolute;
    left: 515px;
    top: 327px;
    height: 123px;
    border-left: 1px solid var(--rule);
    padding-left: 20px;
  }
  .office__address {
    font-size: 22px;
    line-height: 30px;
    margin-bottom: 4px;
  }
</style>
</head>
<body>
  <main class="card">
    <div class="brand">DALWORTH PRYCE</div>

    <section class="person">
      <div class="person__name">Marisol Venner</div>
      <div class="person__role">Account Manager</div>
      <div class="contact-line"><span class="contact-line__label">T</span>713 . 655 . 2048</div>
      <div class="contact-line"><span class="contact-line__label">M</span>832 . 417 . 3095</div>
      <div class="contact-line">mvenner@dalworthpryce.com</div>
    </section>

    <section class="office">
      <div class="office__address">4180 Brambleton Lane, Suite 310<br>Houston, TX 77051</div>
      <div class="contact-line"><span class="contact-line__label">T</span>713 . 508 . 9627</div>
      <div class="contact-line"><span class="contact-line__label">F</span>281 . 369 . 0714</div>
    </section>
  </main>
</body>
</html>
```